Kettle Ledger Business Card design

We need a stand out business card design for Accounting practice based in Australia specialising in pubs, clubs and hotels. We help venues maximise margins, create time and manage cashflow. One club we have been working with for the last 6 months has increased revenue by 3% and margin by 5% in this time frame. We have a back office outsourced system that costs less than having a full time employee and also allows the venues the added benefit of:<br/>-using the office space to become a revenue generating opportunity. <br/>-a complete system to enhance governance, accountability and efficiency within their operation<br/>-52 weeks cover so no hassle to cover annual/sick .. leave<br/><br/>We would like to see designs that use the colours of our logo (green & blue).
Target Market(s)
Australian Pubs, Clubs & Hotels abookkeeping, accounting and tax services
Industry/Entity Type
Accountant
Contact Information for Business Card
Miriam Oakley CPA
Principal
Accountant Tax Agent
Miriam@KettleLedger-example.com.au
0418693142
www.kettleledger-example.com.au
Accounting / Payroll / Tax / SMSF / Technology
Colors
Designer to choose colors to be used in the design.
Look and feel
Each slider illustrates characteristics of the customer's brand and the style your logo design should communicate.

```html
<!DOCTYPE html>
<html lang="en">
<head>
<meta charset="utf-8">
<title>Kettle Ledger Business Card</title>
<link rel="stylesheet" href="https://fonts.googleapis.com/css2?family=Open+Sans:wght@400;600;700&display=swap">
<style>
  :root {
    --ledger-blue: #24408f;
    --ledger-green: #1f7a3c;
    --card-white: #ffffff;
    --backdrop: #ebe8e5;
    --text-light: #ffffff;
  }
  * { box-sizing: border-box; margin: 0; padding: 0; }
  html, body { width: 1200px; height: 997px; overflow: hidden; }
  body {
    background: var(--backdrop);
    font-family: "Open Sans", Arial, sans-serif;
    position: relative;
  }
  .card {
    position: absolute;
    width: 540px;
    height: 328px;
    border-radius: 3px;
    overflow: hidden;
    box-shadow: 0 6px 18px rgba(0,0,0,0.12);
  }
  .card-front { left: 50px; top: 170px; background: var(--card-white); }
  .card-back { left: 610px; top: 500px; background: var(--ledger-blue); }

  .front-panel { position: absolute; inset: 0; }

  .brand {
    display: flex;
    align-items: center;
    gap: 10px;
    font-weight: 700;
    white-space: nowrap;
  }
  .brand-dot { border-radius: 50%; flex: none; }
  .brand-front {
    position: absolute;
    left: 26px;
    top: 92px;
    color: var(--ledger-blue);
    font-size: 26px;
  }
  .brand-front .brand-dot { width: 22px; height: 22px; background: var(--ledger-green); }

  .contact {
    position: absolute;
    left: 272px;
    top: 26px;
    color: var(--text-light);
  }
  .contact-name { font-weight: 700; font-size: 15px; letter-spacing: 0.3px; }
  .contact-role { font-size: 13px; line-height: 17px; margin-top: 3px; }
  .contact-list { list-style: none; margin-top: 20px; font-size: 12.5px; line-height: 18px; }
  .contact-list li { display: flex; align-items: center; gap: 7px; }
  .contact-list svg { width: 10px; height: 10px; flex: none; }
  .services {
    position: absolute;
    left: 272px;
    top: 246px;
    width: 240px;
    color: var(--text-light);
    font-size: 12.5px;
    line-height: 18px;
  }

  .brand-back {
    position: absolute;
    left: 50%;
    top: 50%;
    transform: translate(-50%, -50%);
    color: var(--text-light);
    font-size: 40px;
    gap: 16px;
  }
  .brand-back .brand-dot { width: 34px; height: 34px; background: var(--text-light); }
</style>
</head>
<body>
  <section class="card card-front">
    <svg class="front-panel" width="540" height="328" viewBox="0 0 540 328" aria-hidden="true">
      <polygon fill="var(--ledger-green)" points="240,0 540,0 540,328 240,328 240,64 224,52 240,40"/>
      <polygon fill="var(--ledger-blue)" points="247,0 540,0 540,328 247,328 247,64 231,52 247,40"/>
    </svg>

    <div class="brand brand-front">
      <span class="brand-dot"></span>
      <span class="brand-name">Kettle Ledger</span>
    </div>

    <div class="contact">
      <p class="contact-name">MIRIAM OAKLEY CPA</p>
      <p class="contact-role">Principal<br>Accountant Tax Agent</p>
      <ul class="contact-list">
        <li>
          <svg viewBox="0 0 10 10"><path fill="#fff" d="M2 0.5 L4 2.5 L3 3.7 Q4 6 6.3 7 L7.5 6 L9.5 8 L8.2 9.5 Q3 9 0.5 1.8 Z"/></svg>
          0418693142
        </li>
        <li>
          <svg viewBox="0 0 10 10"><rect x="0.5" y="2" width="9" height="6.5" fill="#fff"/><path d="M0.5 2 L5 5.5 L9.5 2" fill="none" stroke="var(--ledger-blue)" stroke-width="0.9"/></svg>
          Miriam@KettleLedger-example.com.au
        </li>
        <li>
          <svg viewBox="0 0 10 10"><circle cx="5" cy="5" r="4.3" fill="none" stroke="#fff" stroke-width="1"/><ellipse cx="5" cy="5" rx="1.8" ry="4.3" fill="none" stroke="#fff" stroke-width="0.8"/><line x1="0.7" y1="5" x2="9.3" y2="5" stroke="#fff" stroke-width="0.8"/></svg>
          www.kettleledger-example.com.au
        </li>
      </ul>
    </div>

    <p class="services">Accounting / Payroll / Tax /<br>SMSF / Technology</p>
  </section>

  <section class="card card-back">
    <div class="brand brand-back">
      <span class="brand-dot"></span>
      <span class="brand-name">Kettle Ledger</span>
    </div>
  </section>
</body>
</html>
```